Anzeigengestaltung für Estrichbauunternehmen
Zielgruppe
Wir sind ein Estrichbauunternehmen und möchten die Gestaltung einer Stellenanzeige die wir im Internet und Tageszeitungen schalten können beauftragen.
Wir suchen neue Mitarbeiter aus dem Bereich Estrich.
Aufgabenstellung
Die Anzeige soll in einem moderne Design sein mit einem Bild von unseren täglichen Arbeiten. Das Format soll für Zeitungsanzeigen und Internet geeignet sein.

```html
<!DOCTYPE html>
<html lang="de">
<head>
<meta charset="utf-8">
<title>Stellenanzeige – Estrichbau Wendorf GmbH</title>
<link href="https://fonts.googleapis.com/css2?family=Roboto:wght@400;500;700&family=Roboto+Condensed:wght@700&display=swap" rel="stylesheet">
<style>
  :root {
    --brand-blue: #1273b6;
    --text-blue: #1b6eaf;
    --white: #ffffff;
    --photo-dark: #5e5d5b;
    --photo-mid: #8f8d89;
    --photo-light: #c9c7c3;
  }
  * { margin: 0; padding: 0; box-sizing: border-box; }
  html, body { width: 846px; height: 1200px; overflow: hidden; background: var(--white); }
  body { font-family: "Roboto", Arial, sans-serif; color: var(--text-blue); }
  .ad { position: relative; width: 846px; height: 1200px; overflow: hidden; background: var(--white); }

  .intro-band {
    position: absolute; left: 0; top: 0; width: 846px; height: 100px;
    background: var(--brand-blue); color: var(--white);
    padding: 10px 20px 0 30px; font-size: 18px; line-height: 26px; white-space: nowrap;
  }
  .hero {
    position: absolute; left: 0; top: 100px; width: 846px; height: 360px;
    background:
      linear-gradient(180deg, var(--photo-light) 0 6%, transparent 6%),
      radial-gradient(ellipse at 70% 55%, var(--photo-mid) 0%, var(--photo-dark) 70%);
  }
  .hero-headline {
    position: absolute; left: 37px; top: 180px;
    font-family: "Roboto Condensed", "Arial Narrow", sans-serif; font-weight: 700;
    font-size: 60px; line-height: 70px; color: var(--white);
  }

  .lead { position: absolute; left: 40px; top: 505px; font-size: 17px; }
  .job-title {
    position: absolute; left: 39px; top: 528px; white-space: nowrap;
    font-size: 34px; font-weight: 700; color: var(--text-blue);
  }

  .marker { position: absolute; width: 19px; height: 32px; }
  .section-head { position: absolute; font-size: 17.3px; font-weight: 700; white-space: nowrap; }
  .section-head.closing { font-size: 18px; }
  .bullets { position: absolute; list-style: none; font-size: 17.3px; line-height: 22.5px; white-space: nowrap; }
  .bullets li { position: relative; padding-left: 15px; margin-bottom: 4px; }
  .bullets li::before { content: "·"; position: absolute; left: 1px; }

  .contact { position: absolute; left: 34px; top: 1024px; font-size: 17.5px; line-height: 22.3px; font-style: normal; }
  .brand-name {
    position: absolute; left: 470px; top: 1078px;
    display: flex; align-items: center; gap: 12px;
    font-size: 27px; font-weight: 700; color: var(--brand-blue);
  }
  .brand-square { width: 22px; height: 22px; background: var(--brand-blue); }
  .footer-band { position: absolute; left: 0; top: 1172px; width: 846px; height: 28px; background: var(--brand-blue); }
</style>
</head>
<body>
<div class="ad">
  <header class="intro-band">
    Wir sind ein mittelständisches Estrichbau-Unternehmen aus dem Landkreis Hollerbach<br>mit einem Team von 24 Mitarbeiter und mit ca. 350 Bauprojekten im Jahr in diesem<br>Landkreis ein führendes Estrichbauunternehmen.
  </header>

  <div class="hero" role="img" aria-label="Foto: Estrichleger zieht frischen Zementestrich mit einer Glättkelle ab"></div>
  <h1 class="hero-headline">Na, da bewerb‘ ich<br>mich doch glatt!</h1>

  <p class="lead">Zur Verstärkung unseres Teams suchen wir zur sofort oder später:</p>
  <h2 class="job-title">Estrichleger oder komplette Kolonne (m/w/d)</h2>

  <svg class="marker" style="left:0;top:579px" viewBox="0 0 19 32"><polygon points="0,0 19,16 0,32" fill="var(--brand-blue)"/></svg>
  <h3 class="section-head" style="left:35px;top:582px">Unser Tätigkeitsfeld beinhaltet:</h3>
  <ul class="bullets" style="left:35px;top:607px">
    <li>Einbringen von Zementestrichen</li>
    <li>Abziehen und Glätten von Estrichflächen</li>
    <li>Bedienung unserer Förderlogistik</li>
    <li>Verlegung von Wärme- und<br>Trittschalldämmung</li>
  </ul>

  <svg class="marker" style="left:417px;top:579px" viewBox="0 0 19 32"><polygon points="0,0 19,16 0,32" fill="var(--brand-blue)"/></svg>
  <h3 class="section-head" style="left:452px;top:582px">Unsere Erwartungen:</h3>
  <ul class="bullets" style="left:451px;top:607px">
    <li>abgeschl. Berufsausbildung als<br>Estrichleger *innen oder mind. 3 Jahre<br>Berufserfahrung in diesem Beruf</li>
    <li>Führerschein B oder C1E</li>
    <li>Selbstständiges und kundenorientiertes<br>Denken und Handeln</li>
    <li>Zuverlässigkeit, Teamfähigkeit und<br>handwerkliches Geschick</li>
    <li>Körperliche Belastbarkeit,<br>Leistungsbereitschaft und Flexibilität</li>
  </ul>

  <svg class="marker" style="left:0;top:744px" viewBox="0 0 19 32"><polygon points="0,0 19,16 0,32" fill="var(--brand-blue)"/></svg>
  <h3 class="section-head" style="left:35px;top:749px">Wir bieten:</h3>
  <ul class="bullets" style="left:35px;top:774px">
    <li>Eine leistungsgerechte Vergütung gem.<br>den tariflichen Bestimmungen/Akkordlohn</li>
    <li>Ein freundliches und kollegiales Team</li>
    <li>Leistungsbezogene Sonderzahlungen</li>
    <li>Moderne – neuwertige Arbeitsmaschinen u. Fahrzeuge</li>
    <li>Regionale Projekte im Umkreis von 80km (keine Montage)</li>
    <li>Einen sicheren Arbeitsplatz/Unbefristete Arbeitsverträge</li>
    <li>Firmenfahrzeug zur Privatnutzung</li>
  </ul>

  <svg class="marker" style="left:0;top:990px" viewBox="0 0 19 32"><polygon points="0,0 19,16 0,32" fill="var(--brand-blue)"/></svg>
  <h3 class="section-head closing" style="left:35px;top:995px">Wir freuen uns auf ihre schriftliche oder telefonische Bewerbung. Bitte richten sie diese an:</h3>

  <address class="contact">
    Estrichbau Wendorf GmbH<br>
    Jonas Wendorf<br>
    Am Lindenhof 14 · 29847 Birkenried<br>
    www.estrichbau-wendorf.de<br>
    Tel.: 0 47 93 / 73 90 42<br>
    bewerbung@estrichbau-wendorf.de
  </address>

  <div class="brand-name"><span class="brand-square"></span>Estrichbau Wendorf GmbH</div>

  <footer class="footer-band"></footer>
</div>
</body>
</html>
```